Most captivating card ever!

Life Coach - Professional Adventurer - Entrepreneur
I need the worlds most amazing business card for my personal brand. This business card will mostly be used to give to prospective clients for life coaching and business coaching.
Be creative, be adventurous. It needs to stand out. Make people say.. I need this guy!
My background is as an entrepreneur and professional adventurer undertaking extreme expeditions. I am now moving into life coaching.
No specific design ideas, so you have full creativity. Show me your best.
Industry/Entity Type
Life Coaching
Contact Information for Business Card
Dan Pellow
itsdanp.com.au
0468215903
Colors
Designer to choose colors to be used in the design.
Look and feel

```html
<!DOCTYPE html>
<html lang="en">
<head>
<meta charset="utf-8">
<title>Dan Pellow – Business Card</title>
<link href="https://fonts.googleapis.com/css2?family=Asap:wght@400;500&display=swap" rel="stylesheet">
<style>
  :root {
    --bg: #2a2a2c;
    --navy: #0f1527;
    --navy-deep: #0a0f1d;
    --white: #ffffff;
    --blue: #1b9bcf;
    --teal: #17909f;
    --ink: #3a3d44;
  }
  * { margin: 0; padding: 0; box-sizing: border-box; }
  html, body {
    width: 1200px; height: 900px; overflow: hidden;
    background: var(--bg);
    font-family: "Asap", sans-serif;
  }
  .stage {
    width: 1200px; height: 900px;
    display: flex; flex-direction: column;
    align-items: center; justify-content: center; gap: 40px;
  }
  .card {
    position: relative;
    width: 680px; height: 388px;
    border-radius: 22px;
    overflow: hidden;
    box-shadow: 0 14px 34px rgba(0,0,0,0.45);
  }
  /* front */
  .card-front {
    background: linear-gradient(135deg, #141b31 0%, var(--navy) 55%, var(--navy-deep) 100%);
    color: var(--white);
    display: flex; flex-direction: column;
    align-items: center; justify-content: center;
  }
  .card-front .name {
    font-size: 50px; font-weight: 500; letter-spacing: 1px;
  }
  .card-front .tagline {
    margin-top: 14px; font-size: 17px; letter-spacing: 1.5px;
  }
  /* back */
  .card-back { background: var(--white); }
  .card-back .identity {
    position: absolute; left: 92px; top: 96px;
  }
  .card-back .name {
    color: var(--blue);
    font-size: 60px; font-weight: 500; letter-spacing: 1px; line-height: 1;
  }
  .card-back .tagline {
    margin-top: 10px; color: var(--ink);
    font-size: 17px; letter-spacing: 1.5px;
  }
  .contact {
    position: absolute; left: 300px; top: 222px;
    list-style: none; color: var(--ink);
    font-size: 18px; letter-spacing: 1px;
  }
  .contact li { display: flex; align-items: center; gap: 8px; margin-bottom: 6px; }
  .contact svg { width: 18px; height: 18px; }
  .card-base {
    position: absolute; left: 0; bottom: 0; width: 100%; height: 90px;
  }
</style>
</head>
<body>
<main class="stage">
  <section class="card card-front">
    <h1 class="name">Dan Pellow</h1>
    <p class="tagline">Life Coach - Professional Adventurer - Entrepreneur</p>
  </section>

  <section class="card card-back">
    <div class="identity">
      <h2 class="name">Dan Pellow</h2>
      <p class="tagline">Life Coach - Professional Adventurer - Entrepreneur</p>
    </div>
    <ul class="contact">
      <li>
        <svg viewBox="0 0 18 18" aria-hidden="true"><rect x="5" y="1.5" width="8.5" height="15" rx="1.8" fill="none" stroke="#1b9bcf" stroke-width="1.6"/><circle cx="9.25" cy="13.6" r="0.9" fill="#1b9bcf"/></svg>
        0468215903
      </li>
      <li>
        <svg viewBox="0 0 18 18" aria-hidden="true"><g fill="none" stroke="#1b9bcf" stroke-width="1.3"><circle cx="9" cy="9" r="7"/><ellipse cx="9" cy="9" rx="3" ry="7"/><line x1="2" y1="9" x2="16" y2="9"/><line x1="3.2" y1="5.3" x2="14.8" y2="5.3"/><line x1="3.2" y1="12.7" x2="14.8" y2="12.7"/></g></svg>
        itsdanp.com.au
      </li>
    </ul>
    <svg class="card-base" viewBox="0 0 680 90" preserveAspectRatio="none" aria-hidden="true">
      <path d="M0 60 H460 L470 50 H680 V90 H0 Z" fill="#17909f"/>
      <path d="M0 76 H466 L478 64 H680 V90 H0 Z" fill="#ffffff"/>
      <path d="M0 80 H468 L480 68 H680 V90 H0 Z" fill="#0f1527"/>
    </svg>
  </section>
</main>
</body>
</html>
```